Website for Brivex Partners

We need to create a website for our company. Attached is the site map of the website and data input needed. Our theme colour is RED and our Logo is attached

We need a very attractive design where graphics are largely used like flash.

The main idea of the website is to show Telecommunications Suppliers World Wide that we could assist them in getting more business in Africa and Middle East through our local presence in this region.
Updates

Target Market(s)

Telecommunication Suppliers and Clients

Industry/Entity Type

Business

Font styles to use
Serif
Sans Serif

Colors
ec2027

Requirements
Must have
• Graphics that shows Telecommunications Suppliers World Wide that we could assist them in getting more business in Africa and Middle East through our local presence in this region.

The website should be easy to edit for future changes by us.
Nice to have
• New ideas

```html
<!DOCTYPE html>
<html lang="en">
<head>
<meta charset="utf-8">
<title>Brivex Partners</title>
<link href="https://fonts.googleapis.com/css2?family=Open+Sans:wght@300;400;600&display=swap" rel="stylesheet">
<style>
:root{
  --red:#ec2027;
  --red-dark:#c8141b;
  --red-deep:#b3161c;
  --ink:#333333;
  --muted:#6f6f6f;
  --rule:#dddddd;
  --footer:#1e1e1e;
  --footer-base:#2d2d2d;
  --white:#ffffff;
}
*{margin:0;padding:0;box-sizing:border-box}
html,body{width:943px;height:1200px;overflow:hidden;background:var(--white)}
body{font-family:"Open Sans",Arial,sans-serif;color:var(--ink);position:relative}

.top-rule{position:absolute;left:0;top:0;width:943px;height:3px;background:#e4e4e4}

.site-header{position:absolute;left:0;top:3px;width:943px;height:78px}
.brand{position:absolute;left:72px;top:25px;display:flex;align-items:center;gap:10px}
.brand-mark{width:24px;height:24px;background:var(--red)}
.brand-name{font-size:23px;font-weight:600;color:#555555;letter-spacing:.3px;line-height:1}
.support{position:absolute;right:74px;top:24px;text-align:right}
.support-label{font-size:12px;color:#444}
.support-phone{font-size:19px;color:#222;line-height:1.2}

.main-nav{position:absolute;left:0;top:81px;width:943px;height:40px;background:linear-gradient(#ee2a30,#dc1a21)}
.main-nav a{position:absolute;top:0;height:40px;line-height:40px;color:var(--white);text-decoration:none;font-size:13px;text-transform:uppercase}
.main-nav a.is-active{background:var(--red-deep);left:72px;width:78px;text-align:center}

.hero{position:absolute;left:0;top:121px;width:943px;height:369px;overflow:hidden}
.hero-photo{position:absolute;inset:0;background:linear-gradient(90deg,#f3f1ee 0%,#ece7e1 40%,#e6cdb5 62%,#d9b48f 80%,#eee6dc 100%)}
.hero-text{position:absolute;left:75px;top:106px}
.hero-kicker{font-size:24px;font-weight:300;color:var(--red);line-height:1.2}
.hero-title{font-size:39px;font-weight:400;color:var(--red);line-height:1.15;margin-top:1px}
.hero-copy{font-size:10.5px;color:#666;line-height:17px;margin-top:6px;width:330px}
.hero-dots{display:flex;gap:4px;margin-top:14px;margin-left:3px}
.hero-dots span{width:11px;height:11px;border-radius:50%;background:#cfcfcf}
.hero-dots span.is-current{background:var(--red)}

.features{position:absolute;left:0;top:490px;width:943px;height:207px;background:linear-gradient(#ffffff 60%,#f3f3f3);border-top:1px solid #e2e2e2;border-bottom:1px solid #dedede}
.feature-divider{position:absolute;top:0;width:1px;height:206px;background:#e2e2e2}
.feature{position:absolute;top:18px;width:240px}
.feature-image{width:230px;height:94px;border-radius:2px}
.feature-title{font-size:17px;font-weight:400;color:var(--red);margin-top:11px;text-transform:uppercase;letter-spacing:.3px;padding-left:2px}
.feature-copy{font-size:9.5px;color:var(--muted);line-height:16px;padding-left:2px;margin-top:1px;letter-spacing:-.1px}
.features-shadow{position:absolute;left:70px;top:697px;width:800px;height:8px;background:radial-gradient(ellipse at top,rgba(0,0,0,.08),rgba(0,0,0,0) 70%)}

.welcome{position:absolute;left:72px;top:748px;width:530px}
.welcome h1{font-size:22px;font-weight:400;color:#444}
.welcome-lead{font-size:11.3px;color:#333;line-height:17px;margin-top:6px}
.welcome-body{font-size:9.4px;color:var(--muted);line-height:17px;margin-top:10px}

.services-list{position:absolute;left:632px;top:752px;width:198px}
.services-list h2{font-size:20px;font-weight:400;color:var(--red)}
.services-list ul{list-style:none;margin-top:6px}
.services-list li{font-size:10.5px;color:#555;height:23px;line-height:23px;border-bottom:1px solid #e3e3e3;display:flex;align-items:center;gap:6px;padding-left:2px}
.services-list li:last-child{border-bottom:none}
.services-list svg{width:4px;height:7px}

.footer-rule{position:absolute;left:0;top:942px;width:943px;height:4px;background:#e3e3e3}
.site-footer{position:absolute;left:0;top:946px;width:943px;height:204px;background:var(--footer)}
.footer-col{position:absolute;top:36px}
.footer-col h3{font-size:15px;font-weight:400;color:var(--white);text-transform:uppercase}
.footer-col ul{list-style:none;margin-top:4px}
.footer-col li{font-size:10px;color:#e8e8e8;line-height:19px;padding-left:1px}
.footer-note{font-size:10px;color:#e8e8e8;margin-top:5px;line-height:19px}
.social{display:flex;gap:7px;margin-top:8px;padding-left:3px}
.social span{width:19px;height:19px;border-radius:2px}
.social .s1{background:#3b5a98}
.social .s2{background:#3aa9e0}
.social .s3{background:#1e6fa8}
.social .s4{background:#f08a24}

.footer-base{position:absolute;left:0;top:1150px;width:943px;height:50px;background:var(--footer-base)}
.copyright{position:absolute;left:98px;top:18px;font-size:10px;color:#7a7a7a}
</style>
</head>
<body>
<div class="top-rule"></div>

<header class="site-header">
  <div class="brand">
    <span class="brand-mark"></span>
    <span class="brand-name">BRIVEX PARTNERS</span>
  </div>
  <div class="support">
    <div class="support-label">Customer Support</div>
    <div class="support-phone">555.014.2278</div>
  </div>
</header>

<nav class="main-nav">
  <a class="is-active" href="#">Home</a>
  <a href="#" style="left:179px">About Us</a>
  <a href="#" style="left:290px">Services</a>
  <a href="#" style="left:397px">News</a>
  <a href="#" style="left:482px">Blog</a>
  <a href="#" style="left:565px">Support</a>
  <a href="#" style="left:672px">Partners</a>
  <a href="#" style="left:784px">Contact Us</a>
</nav>

<section class="hero">
  <div class="hero-photo" role="img" aria-label="Photo of a smiling woman talking on a mobile phone"></div>
  <div class="hero-text">
    <div class="hero-kicker">Nulla rhoncus dictum metus</div>
    <div class="hero-title">Proin dui lectus cursus</div>
    <p class="hero-copy">Curabitur tristique mi condimentum orci Phasellus pellentesque aliquam enim Proin dui lectus cursus eu mattis</p>
    <div class="hero-dots"><span class="is-current"></span><span></span><span></span><span></span></div>
  </div>
</section>

<section class="features">
  <div class="feature-divider" style="left:338px"></div>
  <div class="feature-divider" style="left:605px"></div>
  <article class="feature" style="left:90px">
    <div class="feature-image" role="img" aria-label="Hand touching a glowing global network" style="background:linear-gradient(135deg,#6c737c,#2a2d33 55%,#8a9099)"></div>
    <h3 class="feature-title">Telecom Services</h3>
    <p class="feature-copy">Lorem ipsum dolor sit amet consectetuer adipiscing elit Nam cursus Morbi ut mi. Nullam enim leo</p>
  </article>
  <article class="feature" style="left:354px">
    <div class="feature-image" role="img" aria-label="Satellite dishes against an evening city sky" style="background:linear-gradient(#5d9be0,#9cc3ec 60%,#3a4050)"></div>
    <h3 class="feature-title">What We Do</h3>
    <p class="feature-copy">Lorem ipsum dolor sit amet consectetuer adipiscing elit Nam cursus Morbi ut mi. Nullam enim leo</p>
  </article>
  <article class="feature" style="left:626px">
    <div class="feature-image" role="img" aria-label="Hand holding a tablet with a glowing globe" style="background:linear-gradient(135deg,#2f6fa8,#6fb0dd 50%,#1d4f80)"></div>
    <h3 class="feature-title">Why Choose Us</h3>
    <p class="feature-copy">Lorem ipsum dolor sit amet consectetuer adipiscing elit Nam cursus Morbi ut mi. Nullam enim leo</p>
  </article>
</section>
<div class="features-shadow"></div>

<section class="welcome">
  <h1>Welcome to Our Website Mainpage</h1>
  <p class="welcome-lead">Pellentesque faucibus Ut accumsan ultricies elit Maecenas at justo id velit placerat molestie Donec dictum lectus non odio Cras a ante vitae enim iaculis aliquam</p>
  <p class="welcome-body">Mauris vel lacus vitae felis vestibulum volutpat Etiam est nunc venenatis in tristique eu imperdiet ac nisl Cum sociis natoque penatibus et magnis dis parturient montes nascetur ridiculus mus In iaculis facilisis massa Etiam eu urna Sed porta Suspendisse quam leo molestie sed luctus quis feugiat in pede Fusce tellus Sed metus augue convallis et vehicula ut pulvinar eu ante Integer orci tellus tristique vitae consequat nec porta vel lectus</p>
</section>

<aside class="services-list">
  <h2>Services We Provide</h2>
  <ul>
    <li><svg viewBox="0 0 4 7"><path d="M0 0L4 3.5L0 7Z" fill="#777"/></svg>Phasellus felis dolor scelerisque</li>
    <li><svg viewBox="0 0 4 7"><path d="M0 0L4 3.5L0 7Z" fill="#777"/></svg>Tempus eget lobortis id libero.</li>
    <li><svg viewBox="0 0 4 7"><path d="M0 0L4 3.5L0 7Z" fill="#777"/></svg>Nec erat at purus cursus interdum.</li>
    <li><svg viewBox="0 0 4 7"><path d="M0 0L4 3.5L0 7Z" fill="#777"/></svg>Vestibulum ligula augue</li>
    <li><svg viewBox="0 0 4 7"><path d="M0 0L4 3.5L0 7Z" fill="#777"/></svg>Maecenas at justo id velit</li>
  </ul>
</aside>

<div class="footer-rule"></div>
<footer class="site-footer">
  <div class="footer-col" style="left:110px">
    <h3>Company</h3>
    <ul><li>What We Do</li><li>Why Choose Us</li><li>Features</li><li>Plans</li><li>Products</li></ul>
  </div>
  <div class="footer-col" style="left:276px">
    <h3>Services</h3>
    <ul><li>Aliquam nec erat</li><li>At purus cursus</li><li>Interdum Vestibulum</li><li>Ligula augue</li><li>Bibendum accumsan</li></ul>
  </div>
  <div class="footer-col" style="left:464px">
    <h3>Support</h3>
    <ul><li>Aliquam nec erat</li><li>At purus cursus</li><li>Interdum Vestibulum</li><li>Ligula augue</li><li>Bibendum accumsan</li></ul>
  </div>
  <div class="footer-col" style="left:640px">
    <h3>Get Connected</h3>
    <p class="footer-note">Please stay in touch with us on followings.</p>
    <div class="social"><span class="s1"></span><span class="s2"></span><span class="s3"></span><span class="s4"></span></div>
  </div>
</footer>
<div class="footer-base">
  <p class="copyright">© 2014 Company Name &nbsp;All right reserved &nbsp;Term of Use</p>
</div>
</body>
</html>
```